Business Card Design

we are a small based family business that specialise in 12v led lights for kelvo caravans.
we also sell 12v switches, wire, circuit breakers, dimmers etc but our main line is LEDs.
We would like something that reflects the LED lighting on our cards.
www.willowtreeleds.com.au is where you can have a look at to get ideas, of our product.
I have attached the logo we generally use on all our tradio listings and is the main header on our website.

Look forward to seeing what your team comes up with.

Industry/Entity Type

Business

Contact Information for Business Card

Tam 0491 738 205
Cedarwood Vale QLD 4312

www.willowtreeleds.com

```html
<!DOCTYPE html>
<html lang="en">
<head>
<meta charset="utf-8">
<title>Willow Tree LEDs – Business Card</title>
<link rel="stylesheet" href="https://fonts.googleapis.com/css2?family=Cinzel:wght@400;700&display=swap">
<style>
  :root {
    --card-bg: #ffffff;
    --panel-red-light: #9a0202;
    --panel-red-mid: #7a0303;
    --panel-red-dark: #4a0101;
    --panel-text: #f3e6e6;
    --brand-red: #a00f0f;
    --bulb-pink: #e9c4c4;
  }
  * { margin: 0; padding: 0; box-sizing: border-box; }
  html, body {
    width: 1200px;
    height: 741px;
    overflow: hidden;
    background: var(--card-bg);
  }
  .card {
    position: relative;
    width: 1200px;
    height: 741px;
    background: var(--card-bg);
    font-family: "Cinzel", serif;
  }
  .contact-panel {
    position: absolute;
    left: 70px;
    top: 82px;
    width: 529px;
    height: 576px;
    background: linear-gradient(180deg, var(--panel-red-light) 0%, var(--panel-red-mid) 55%, var(--panel-red-dark) 100%);
  }
  .contact-details {
    position: absolute;
    left: 39px;
    top: 348px;
    width: 450px;
    color: var(--panel-text);
    font-size: 22px;
    line-height: 37px;
    letter-spacing: 3.5px;
    text-transform: uppercase;
  }
  .website {
    position: absolute;
    left: 18px;
    top: 482px;
    display: flex;
    align-items: center;
    gap: 6px;
    color: var(--panel-text);
    font-size: 22px;
    letter-spacing: 3px;
    text-transform: uppercase;
  }
  .website-icon { width: 46px; height: 34px; flex: none; }
  .brand-name {
    position: absolute;
    left: 660px;
    top: 116px;
    width: 460px;
    text-align: center;
    color: var(--brand-red);
    font-weight: 700;
    font-size: 52px;
    line-height: 56px;
    letter-spacing: 1px;
    text-transform: uppercase;
  }
  .bulb-art {
    position: absolute;
    left: 777px;
    top: 275px;
    width: 211px;
    height: 305px;
    background: var(--bulb-pink);
    border-radius: 40px 40px 105px 105px;
  }
</style>
</head>
<body>
  <div class="card">
    <section class="contact-panel" role="img" aria-label="Deep red background with water droplets on glass">
      <p class="contact-details">Tam 0491 738 205 Cedarwood Vale QLD 4312</p>
      <p class="website">
        <svg class="website-icon" viewBox="0 0 46 34" aria-hidden="true">
          <g fill="none" stroke="#f3e6e6" stroke-width="2">
            <circle cx="15" cy="15" r="12"/>
            <ellipse cx="15" cy="15" rx="5" ry="12"/>
            <line x1="3" y1="15" x2="27" y2="15"/>
            <line x1="5" y1="9" x2="25" y2="9"/>
            <line x1="5" y1="21" x2="25" y2="21"/>
            <circle cx="29" cy="20" r="6" fill="#7a0303"/>
          </g>
          <line x1="33" y1="24" x2="43" y2="32" stroke="#f3e6e6" stroke-width="4" stroke-linecap="round"/>
        </svg>
        <span>www.willowtreeleds.com</span>
      </p>
    </section>

    <h1 class="brand-name">Willow Tree<br>LEDs</h1>

    <div class="bulb-art" role="img" aria-label="Soft pink light bulb illustration"></div>
  </div>
</body>
</html>
```